Marketing Flyer for Coaching Company

Need a marketing flyer I can use based off of my website Quillmoorcoaching.com. Quick Summary of me include "over 40,000 hours of leadership and coaching experience" Talking about the three services offered. Career and life coaching / Steady Oak Callback / Fractional Sales Leadership. I would love to use the colors from the logo. I do not want pricing included.

Target Market(s)

Therapist Offices and other professional treatment centers

Industry/Entity Type

Coaching

Other font styles liked:
• Hero Light Regular

Colors
0054AA
0677BA
7BADD7
CADEEF
E8F1F8
0094D4
00A9DD
6FCCEA
C7EBF8
E9F6FB
00AB8E
00BBA5
67D7C9
C6EFE9
E9F9F6
59FF00
82FF00
B8FF75
E3FFCB
F4FFEA
FFF300
FFF600
FEFA6F
FFFEC7
FFFEE8
EB3D1F
EC4F4E
F09395
F8D3D4
FCEDEE
E54698
E96AAD
F1A4CE
F9D9EA
FCEFF6
A7469A
B969AE
D3A5CF
EDDBEB
F8F0F9
6B429C
8869AF
B7A5CE
E3DAEB
F3F0F8

Requirements
Must have
• Logo "over 40,000 hours of leadership and coaching experience" Talking about the three services offered. Career and life coaching / Steady Oak Callback / Fractional Sales Leadership. I would love to use the colors from the logo. Contact info
Nice to have
• Color Pallet based off of logo pallet id's are in the attachments
Should not have
• Pricing

```html
<!DOCTYPE html>
<html lang="en">
<head>
<meta charset="utf-8">
<title>Quillmoor Coaching – Flyer</title>
<link rel="stylesheet" href="https://fonts.googleapis.com/css2?family=Lora:wght@400;500&family=Libre+Baskerville:ital@1&display=swap">
<style>
  :root {
    --ink: #1f1f24;
    --navy: #1d1846;
    --plum: #5a2d62;
    --icon: #5b2b6b;
    --magenta: #9b1b5e;
    --lime: #b5c73e;
    --paper: #ffffff;
  }
  * { margin: 0; padding: 0; box-sizing: border-box; }
  html, body { width: 851px; height: 1200px; overflow: hidden; background: var(--paper); }
  .flyer { position: relative; width: 851px; height: 1200px; background: var(--paper); color: var(--ink); font-family: "Lora", Georgia, serif; }
  .abs { position: absolute; }
  .centered { left: 0; width: 100%; text-align: center; }
  .serif-italic { font-family: "Libre Baskerville", "Times New Roman", serif; font-style: italic; }
  .rule { position: absolute; height: 2px; background: var(--plum); }

  .brand-mark { left: 405px; top: 36px; width: 42px; height: 42px; border-radius: 50%; background: var(--plum); }
  .brand-name { top: 100px; font-size: 36px; line-height: 44px; font-weight: 400; color: var(--navy); }
  .tagline { top: 186px; font-size: 14px; line-height: 20px; }
  .headline { top: 220px; font-size: 38px; line-height: 43px; font-weight: 400; }
  .subhead { top: 328px; font-size: 16.5px; line-height: 24px; }

  .band { position: absolute; top: 380px; height: 10px; }
  .band--left { left: 0; width: 254px; background: var(--magenta); }
  .band--mid { left: 254px; width: 343px; background: var(--lime); }
  .band--right { left: 597px; width: 254px; background: var(--magenta); }

  .intro { left: 46px; width: 759px; top: 442px; font-size: 16.5px; line-height: 22px; text-align: center; }

  .section-title { top: 566px; font-size: 32px; line-height: 42px; font-weight: 400; }

  .service { position: absolute; top: 608px; width: 232px; text-align: center; }
  .service__icon { display: block; margin: 0 auto; width: 60px; height: 58px; }
  .service__name { margin-top: 16px; font-size: 15px; line-height: 22px; font-weight: 400; white-space: nowrap; }
  .service__rule { width: 154px; height: 2px; background: var(--plum); margin: 5px auto 6px; }
  .service__text { width: 204px; margin: 0 auto; font-family: "Libre Baskerville", "Times New Roman", serif; font-style: italic; font-size: 12px; line-height: 15.5px; }

  .why-title { top: 873px; font-size: 24px; line-height: 30px; font-weight: 400; }
  .why-list { left: 157px; top: 909px; list-style: none; }
  .why-list li { display: flex; align-items: center; height: 23.5px; font-size: 14.5px; white-space: nowrap; }
  .why-list svg { width: 16px; height: 16px; margin-right: 13px; margin-top: 6px; }

  .closing { top: 1016px; font-size: 19px; line-height: 24px; }

  .contact-bar { position: absolute; left: 0; top: 1057px; width: 851px; height: 30px; background: var(--lime); }
  .contact-bar span { position: absolute; top: 0; font-family: "Libre Baskerville", "Times New Roman", serif; font-style: italic; font-size: 16px; line-height: 30px; color: var(--ink); white-space: nowrap; }
  .phone { top: 1105px; font-size: 36px; line-height: 46px; font-weight: 400; }
</style>
</head>
<body>
<main class="flyer">
  <header>
    <div class="abs brand-mark" aria-hidden="true"></div>
    <div class="abs centered brand-name">Quillmoor Coaching</div>
    <div class="rule" style="left:285px; top:178px; width:281px;"></div>
    <p class="abs centered tagline serif-italic">Transforming Potential Into Purpose</p>
    <h1 class="abs centered headline">Over 40,000 Hours of<br>Leadership &amp; Coaching Experience</h1>
    <div class="rule" style="left:139px; top:319px; width:573px;"></div>
    <p class="abs centered subhead serif-italic">Guiding professionals to clarity, confidence &amp; growth.</p>
  </header>

  <div class="band band--left"></div>
  <div class="band band--mid"></div>
  <div class="band band--right"></div>

  <p class="abs intro serif-italic">At Quillmoor Coaching, we help individuals and teams navigate change, build resilience, and step confidently into what’s next — professionally and personally. With decades of real-world leadership experience, our approach is grounded in insight, empathy, and meaningful results.</p>

  <div class="rule" style="left:70px; top:586px; width:246px;"></div>
  <h2 class="abs centered section-title">Our Services</h2>
  <div class="rule" style="left:535px; top:586px; width:246px;"></div>

  <section class="service" style="left:68px;">
    <svg class="service__icon" viewBox="0 0 60 58" aria-hidden="true">
      <g fill="none" stroke="var(--icon)">
        <circle cx="26" cy="32" r="23" stroke-width="5"/>
        <circle cx="26" cy="32" r="13" stroke-width="5"/>
      </g>
      <circle cx="26" cy="32" r="5" fill="var(--icon)"/>
      <path d="M26 32 L48 10" stroke="var(--icon)" stroke-width="4" stroke-linecap="round"/>
      <path d="M44 8 L52 2 L50 10 L58 8 L50 16 L42 16 Z" fill="var(--icon)"/>
    </svg>
    <h3 class="service__name">Career &amp; Life Coaching</h3>
    <div class="service__rule"></div>
    <p class="service__text">Personalized coaching to unlock your strengths, clarify direction, and accelerate purposeful action. Whether you’re growing into leadership or navigating a major transition, we walk with you every step of the way.</p>
  </section>

  <section class="service" style="left:309px;">
    <svg class="service__icon" viewBox="0 0 60 58" aria-hidden="true">
      <g fill="none" stroke="var(--icon)" stroke-width="3" stroke-linejoin="round">
        <path d="M30 6 h22 a6 6 0 0 1 6 6 v12 a6 6 0 0 1 -6 6 h-2 l2 6 l-8 -6 h-14 a6 6 0 0 1 -6 -6 v-12 a6 6 0 0 1 6 -6 z" fill="#fff"/>
        <path d="M36 14 h16 M32 19 h20 M34 24 h14" stroke-width="2"/>
        <path d="M10 24 h22 a7 7 0 0 1 7 7 v10 a7 7 0 0 1 -7 7 h-14 l-9 6 l2 -7 a7 7 0 0 1 -8 -6 v-10 a7 7 0 0 1 7 -7 z" fill="#fff"/>
      </g>
      <g fill="var(--icon)"><circle cx="14" cy="36" r="2"/><circle cx="21" cy="36" r="2"/><circle cx="28" cy="36" r="2"/></g>
    </svg>
    <h3 class="service__name">Professional Steady Oak Callback</h3>
    <div class="service__rule" style="width:228px;"></div>
    <p class="service__text">Sometimes you don’t need a long program — just a trusted partner to talk through a challenge, decision, or doubt. Honest conversation. No judgment. Just clarity.</p>
  </section>

  <section class="service" style="left:550px;">
    <svg class="service__icon" viewBox="0 0 60 58" aria-hidden="true">
      <g fill="var(--icon)">
        <rect x="2" y="44" width="6" height="10"/><rect x="10" y="38" width="6" height="16"/>
        <rect x="18" y="34" width="6" height="20"/><rect x="26" y="40" width="6" height="14"/>
        <rect x="34" y="44" width="6" height="10"/><rect x="42" y="34" width="6" height="20"/>
        <rect x="50" y="26" width="6" height="28"/>
      </g>
      <path d="M2 36 L18 26 L32 34 L54 14" fill="none" stroke="var(--icon)" stroke-width="2.5"/>
      <path d="M48 12 L58 8 L55 18 Z" fill="var(--icon)"/>
    </svg>
    <h3 class="service__name">Fractional Sales Leadership</h3>
    <div class="service__rule" style="width:156px;"></div>
    <p class="service__text">Need senior sales leadership without the full-time commitment? Bring in seasoned leadership to mentor teams, refine strategy, and elevate performance.</p>
  </section>

  <div class="rule" style="left:121px; top:860px; width:636px;"></div>
  <h2 class="abs centered why-title">Why Quillmoor?</h2>
  <ul class="abs why-list serif-italic">
    <li><svg viewBox="0 0 16 16" aria-hidden="true"><path d="M2 8 L6 13 L14 2" fill="none" stroke="var(--plum)" stroke-width="1.5"/></svg>Over 40,000 hours of leadership &amp; coaching experience</li>
    <li><svg viewBox="0 0 16 16" aria-hidden="true"><path d="M2 8 L6 13 L14 2" fill="none" stroke="var(--plum)" stroke-width="1.5"/></svg>Deep understanding of professional and personal growth</li>
    <li><svg viewBox="0 0 16 16" aria-hidden="true"><path d="M2 8 L6 13 L14 2" fill="none" stroke="var(--plum)" stroke-width="1.5"/></svg>Tailored support for transitions, teams, and leadership challenges</li>
  </ul>

  <div class="rule" style="left:76px; top:1027px; width:218px;"></div>
  <p class="abs centered closing">Connect. Clarify. Grow.</p>
  <div class="rule" style="left:550px; top:1027px; width:218px;"></div>

  <div class="contact-bar">
    <span style="left:196px;">Quillmoorcoaching.com</span>
    <span style="left:420px;">info@quillmoorcoaching.com</span>
  </div>
  <p class="abs centered phone">(555) 014-2290</p>
</main>
</body>
</html>
```